Vask - Website Design in WordPress (2 pages)

The goal of this design work is to create two highly focused, PPC- and SEO-aware landing pages that clearly explain the experience in familiar terms and drive app installs. The design must respect the existing visual identity and support future iteration of copy and content without requiring redesign.
Required Deliverables:
Fully working WordPress site containing:
Homepage template
Location landing page template
Mobile-first, responsive
CTA behaviour exactly as designed
Required
WordPress admin access
Full site export / backup
Homepage template
Mobile-first behaviour
CTA visible above the fold on mobile
Uses my:
Visual identity
Logo
Placeholder copy
I receive:
Admin access
Full site export / backup
Not acceptable
20+ plugins
Proprietary or abandoned builders
Hardcoded layouts that can’t be reused
Separate page designs per location
Elementor is preferred if:
One builder only
Clean structure
No custom lock-in widgets
Uploaded the mobile design for inspiration only

```html
<!DOCTYPE html>
<html lang="en">
<head>
<meta charset="utf-8">
<title>Vask – Play City Adventures in Bristol</title>
<link href="https://fonts.googleapis.com/css2?family=Outfit:wght@600;700;800&family=Poppins:wght@400;500;600&display=swap" rel="stylesheet">
<style>
:root{
  --teal:#1a7d8c;
  --teal-dark:#166f7d;
  --teal-light:#7fc1cc;
  --ink:#2d3136;
  --ink-soft:#5b6168;
  --dark:#30353b;
  --sky:#dcedf4;
  --sky-mid:#b9dcec;
  --white:#ffffff;
  --line:#d9dde0;
}
*{box-sizing:border-box;margin:0;padding:0}
html,body{width:1200px;height:3272px;overflow:hidden}
body{position:relative;background:var(--white);font-family:"Poppins",sans-serif;color:var(--ink)}
.abs{position:absolute}
.heading{font-family:"Outfit",sans-serif;font-weight:800;color:var(--ink);letter-spacing:-0.5px;text-transform:uppercase}

/* footer background + white lobe */
.footer-bg{left:0;top:2470px;width:1200px;height:802px;background:var(--dark)}
.page-lobe{left:0;top:1300px;width:1200px;height:1660px;background:var(--white);border-bottom-left-radius:520px 500px;border-bottom-right-radius:330px 260px}

/* hero */
.hero-accent{right:0;top:380px;width:520px;height:340px;background:var(--sky-mid)}
.hero{left:0;top:0;width:1200px;height:694px;background:linear-gradient(180deg,#e2eef3 0%,#eef5f8 45%,#ffffff 100%);border-bottom-right-radius:340px 300px}
.logo{left:133px;top:20px;font-family:"Outfit",sans-serif;font-weight:700;font-size:46px;color:var(--teal);letter-spacing:-1px}
.nav{top:34px;font-size:13px;color:var(--ink-soft)}
.nav a{position:absolute;white-space:nowrap;color:inherit;text-decoration:none}
.btn-outline{left:841px;top:20px;width:134px;height:41px;border:1px solid var(--ink);border-radius:21px;font-size:12px;display:flex;align-items:center;justify-content:center;font-weight:500}
.avail{left:985px;top:27px;font-size:11px;line-height:13px;font-weight:500;white-space:nowrap}
.hero-title{left:133px;top:200px;font-size:37px;line-height:45px;white-space:nowrap;letter-spacing:-1px}
.hero-text{left:133px;top:346px;width:420px;font-size:13.5px;line-height:19px;color:var(--ink)}
.store{height:44px;border-radius:22px;background:var(--ink);color:var(--white);display:flex;align-items:center;gap:8px;padding-left:16px}
.store .dot{width:18px;height:18px;border-radius:50%;background:var(--teal-light)}
.store small{display:block;font-size:7px;line-height:8px;text-transform:uppercase;white-space:nowrap}
.store b{display:block;font-size:13px;font-weight:500;line-height:14px}
.store-light{background:var(--white);color:var(--ink)}
.store-light .dot{background:var(--teal)}
.scroll-cue{left:133px;top:519px;width:37px;height:59px;border:1px solid var(--ink);border-radius:19px}
.photo{background:linear-gradient(135deg,#c9a98a,#5d6a74)}
.hero-photo-main{left:597px;top:137px;width:234px;height:464px;border-radius:70px 0 0 200px;background:linear-gradient(160deg,#d8b59a 0%,#8c6d5a 55%,#3e4a57 100%)}
.hero-photo-phones{left:831px;top:137px;width:233px;height:231px;border-radius:0 116px 116px 0;background:linear-gradient(135deg,#e7e2d6,#d8cfbd)}
.hero-photo-city{left:831px;top:368px;width:233px;height:233px;border-radius:0 116px 116px 0;background:linear-gradient(135deg,#4f6e5c,#2f4a3f 60%,#5e8a52)}

/* why section */
.why{left:0;top:693px;width:1200px;height:571px;border-radius:270px 0 280px 0;background:linear-gradient(180deg,#cfe4ec 0%,#b7d6e2 50%,#a6c8d4 100%)}
.why-title{left:0;top:785px;width:1200px;text-align:center;font-size:30px}
.card{top:852px;height:264px;background:var(--white);border-radius:16px;overflow:hidden}
.card .thumb{height:138px}
.card h3{font-family:"Outfit",sans-serif;font-weight:700;font-size:13.5px;line-height:16px;text-transform:uppercase;margin:18px 20px 8px}
.card p{font-size:11px;line-height:16px;color:var(--ink-soft);margin:0 20px}
.card-intro h3{margin-top:20px}
.mark{width:40px;height:40px;border-radius:50%;background:var(--teal);margin:26px 0 0 23px}
.arrow-btn{top:1156px;width:48px;height:48px;border-radius:50%;display:flex;align-items:center;justify-content:center}

/* experience */
.exp-photo{left:246px;top:1339px;width:393px;height:391px;border-radius:0 200px 200px 200px;background:linear-gradient(150deg,#c29a7d,#7b5d4c 55%,#3d5e63)}
.exp-map{left:180px;top:1537px;width:206px;height:206px;border-radius:50%;background:linear-gradient(135deg,#eceeef,#d7dbdd);border:5px solid var(--white)}
.exp-title{left:715px;top:1378px;font-size:31px;line-height:31px;white-space:nowrap}
.feat{left:715px;display:flex;gap:13px}
.feat svg{width:44px;height:46px;flex:none}
.feat h4,.step h4{font-family:"Outfit",sans-serif;font-weight:700;font-size:14px;line-height:17px;text-transform:uppercase;margin-top:2px;white-space:nowrap}
.feat p,.step p{font-size:12px;line-height:17px;color:var(--ink-soft);margin-top:3px;white-space:nowrap}

/* steps */
.steps-title{left:190px;top:1860px;font-size:31px;white-space:nowrap}
.step{left:186px;display:flex;gap:16px}
.step svg{width:42px;height:50px;flex:none}
.divider{left:243px;width:264px;height:1px;background:var(--line)}
.steps-photo-big{left:611px;top:1791px;width:272px;height:425px;border-radius:136px;background:linear-gradient(160deg,#5a4336,#a4453b 55%,#6d4d38)}
.steps-photo-small{left:843px;top:1890px;width:170px;height:271px;border-radius:85px;border:4px solid var(--white);background:linear-gradient(160deg,#8e8b86,#4a433c 60%,#b59b78)}
.play{left:571px;top:2077px;width:81px;height:81px;border-radius:50%;background:var(--teal);display:flex;align-items:center;justify-content:center}

/* safe */
.safe-photo{left:273px;top:2241px;width:295px;height:363px;border-radius:150px 150px 150px 0;background:linear-gradient(150deg,#b07a5e,#d6b49b 50%,#7b5644)}
.safe-title{left:608px;top:2364px;font-size:31px;line-height:34px;white-space:nowrap}
.bullets{left:608px;top:2446px;list-style:none;font-size:12px;color:var(--ink-soft);white-space:nowrap}
.bullets li{display:flex;align-items:center;gap:8px;height:22.5px}
.bullets li span{width:11px;height:11px;border-radius:50%;background:var(--teal);display:inline-flex;align-items:center;justify-content:center}

/* CTA */
.cta-outer{left:133px;top:2693px;width:931px;height:181px;border-radius:91px;background:#8fc6cf}
.cta-inner{left:218px;top:2693px;width:766px;height:181px;border-radius:91px;background:linear-gradient(90deg,#1b7b89,#237f8d 60%,#1d7684)}
.cta-title{left:287px;top:2750px;font-size:29px;line-height:33px;color:var(--white);white-space:nowrap}

/* footer */
.foot-logo{left:133px;top:2978px;font-family:"Outfit",sans-serif;font-weight:700;font-size:100px;line-height:100px;color:var(--white);letter-spacing:-3px}
.foot-col{color:#c3c8cc;font-size:10.5px;line-height:18.7px;white-space:nowrap}
.foot-col h5{font-family:"Outfit",sans-serif;font-weight:700;font-size:13px;color:var(--white);text-transform:uppercase;margin-bottom:10px}
.contact-item{display:flex;gap:8px;margin-bottom:10px;line-height:14px}
.contact-item small{display:block;font-size:9px;color:var(--white);text-transform:uppercase}
.social{top:3011px;width:43px;height:43px;border-radius:50%;background:#464b51;display:flex;align-items:center;justify-content:center}
.social span{width:10px;height:10px;border-radius:50%;background:var(--white)}
.foot-line{left:169px;top:3213px;width:861px;height:1px;background:#555b61}
.copyright{left:0;top:3231px;width:1200px;text-align:center;font-size:9px;color:#c3c8cc;text-transform:uppercase}
.chat{left:1104px;top:3191px;width:49px;height:48px;border-radius:24px 24px 24px 6px;background:var(--teal);display:flex;align-items:center;justify-content:center}
</style>
</head>
<body>

<div class="abs footer-bg"></div>
<div class="abs page-lobe"></div>

<!-- Hero -->
<div class="abs hero-accent"></div>
<header class="abs hero">
  <div class="abs logo">vask</div>
  <nav class="abs nav">
    <a style="left:415px">How it Works</a>
    <a style="left:523px">Experiences</a>
    <a style="left:625px">Cities</a>
    <a style="left:687px">FAQ</a>
    <a style="left:742px">Support</a>
  </nav>
  <div class="abs btn-outline">Download App</div>
  <div class="abs avail">Available on<br>phones &amp; tablets</div>

  <h1 class="abs heading hero-title">Play city adventures<br>in Bristol — walk,<br>explore, and solve!</h1>
  <p class="abs hero-text">Download the Vask app to experience exciting outdoor group games with friends. Discover real locations, follow the story, and complete challenges in your city</p>
  <div class="abs store" style="left:135px;top:427px;width:145px"><i class="dot"></i><div><small>Get it on</small><b>App Shelf</b></div></div>
  <div class="abs store" style="left:286px;top:427px;width:145px"><i class="dot"></i><div><small>Download on the</small><b>Play Hub</b></div></div>
  <div class="abs scroll-cue">
    <svg width="37" height="59" viewBox="0 0 37 59"><path d="M18 22v16M13 33l5 5 5-5" stroke="#2d3136" stroke-width="1.3" fill="none"/></svg>
  </div>

  <div class="abs hero-photo-main" role="img" aria-label="Group of smiling friends looking at a red phone"></div>
  <div class="abs hero-photo-phones" role="img" aria-label="Three phone screens numbered 01, 02, 03"></div>
  <div class="abs hero-photo-city" role="img" aria-label="Aerial view of city streets and trees"></div>
</header>

<!-- Why section -->
<section class="abs why" role="img" aria-label="Faded aerial view of Bristol coastline and harbour"></section>
<h2 class="abs heading why-title">Why Vask stands out in Bristol</h2>

<article class="abs card card-intro" style="left:212px;width:182px">
  <div class="mark"></div>
  <h3>Download<br>Vask app</h3>
  <p>Download the Vask app and experience outdoor group adventures in your city with friends. Walk, solve, and explore real locations...</p>
</article>
<article class="abs card" style="left:414px;width:189px">
  <div class="thumb photo" role="img" aria-label="Colourful city playground structure" style="background:linear-gradient(160deg,#6a9bc5,#d9a13a 60%,#7d6a48)"></div>
  <h3>City as your<br>playground</h3>
  <p>Explore streets, landmarks, and hidden spots.</p>
</article>
<article class="abs card" style="left:615px;width:188px">
  <div class="thumb photo" role="img" aria-label="Excited group of kids indoors" style="background:linear-gradient(160deg,#7a4e36,#b3876a 55%,#3e3a3c)"></div>
  <h3>Better than escape<br>rooms</h3>
  <p>No fixed schedule, no equipment needed.</p>
</article>
<article class="abs card" style="left:814px;width:189px">
  <div class="thumb photo" role="img" aria-label="Friends taking a selfie in a sunny park" style="background:linear-gradient(160deg,#c9d27a,#8f9e4c 50%,#a86a52)"></div>
  <h3>Flexible &amp;<br>replayable</h3>
  <p>Play anytime with friends or family.</p>
</article>

<div class="abs arrow-btn" style="left:549px;background:#7fb2bb">
  <svg width="12" height="12" viewBox="0 0 12 12"><path d="M7.5 2.5 4 6l3.5 3.5" stroke="#2d3136" stroke-width="1.5" fill="none"/></svg>
</div>
<div class="abs arrow-btn" style="left:602px;background:var(--white)">
  <svg width="12" height="12" viewBox="0 0 12 12"><path d="M4.5 2.5 8 6 4.5 9.5" stroke="#2d3136" stroke-width="1.5" fill="none"/></svg>
</div>

<!-- Experience -->
<div class="abs exp-photo" role="img" aria-label="Four friends laughing together while looking at a phone"></div>
<div class="abs exp-map" role="img" aria-label="Street map with a blue walking route and location pins"></div>

<h2 class="abs heading exp-title">Experience the fun<br>&amp; adventure</h2>

<div class="abs feat" style="top:1466px">
  <svg viewBox="0 0 44 46" fill="none" stroke="#1a7d8c" stroke-width="1.6"><rect x="10" y="2" width="22" height="34" rx="4"/><path d="M18 14v10l8-5z"/><path d="M4 30v12h8"/></svg>
  <div><h4>Social play</h4><p>Team up with friends and compete.</p></div>
</div>
<div class="abs feat" style="top:1524px">
  <svg viewBox="0 0 44 46" fill="none" stroke="#1a7d8c" stroke-width="1.6"><path d="M12 6 3 40M12 6l10 34M12 6v34"/><circle cx="34" cy="10" r="4"/><path d="M34 2v3M34 15v3M26 10h3M39 10h3"/><path d="M22 40l8-12 8 12"/></svg>
  <div><h4>Active &amp; outdoor</h4><p>Walk and discover your city.</p></div>
</div>
<div class="abs feat" style="top:1583px">
  <svg viewBox="0 0 44 46" fill="none" stroke="#1a7d8c" stroke-width="1.6"><path d="M22 44V6M16 12l6-6 6 6M22 24 8 16M8 16v6M8 16h6M22 24l14-8M36 16v6M36 16h-6"/></svg>
  <div><h4>Easy &amp; flexible</h4><p>Play at your own pace, anytime.</p></div>
</div>
<div class="abs feat" style="top:1642px">
  <svg viewBox="0 0 44 46" fill="none" stroke="#1a7d8c" stroke-width="1.6"><circle cx="22" cy="6" r="4"/><path d="M12 16h20M22 12v16M16 40l6-12 6 12M10 44h24M14 40h16"/></svg>
  <div><h4>Engaging challenges</h4><p>Each game is unique and replayable.</p></div>
</div>

<!-- Steps -->
<h2 class="abs heading steps-title">Start in 4 easy steps</h2>

<div class="abs step" style="top:1911px">
  <svg viewBox="0 0 42 50" fill="none" stroke="#1a7d8c" stroke-width="1.6"><rect x="8" y="2" width="26" height="46" rx="4"/><path d="M21 14v16M15 24l6 6 6-6M14 36h14"/></svg>
  <div><h4>1. Download the app</h4><p>Available on phones &amp; tablets.</p></div>
</div>
<div class="abs divider" style="top:1974px"></div>
<div class="abs step" style="top:1988px">
  <svg viewBox="0 0 42 50" fill="none" stroke="#1a7d8c" stroke-width="1.6"><rect x="2" y="4" width="20" height="16"/><path d="M6 12l4 4 8-10"/><rect x="2" y="24" width="16" height="14"/><path d="M24 26v16l6 6h8V34l-8-2V22a3 3 0 0 0-6 0z"/></svg>
  <div><h4>2. Pick your city &amp; adventure</h4><p>Choose a game near you.</p></div>
</div>
<div class="abs divider" style="top:2047px"></div>
<div class="abs step" style="top:2061px">
  <svg viewBox="0 0 42 50" fill="none" stroke="#1a7d8c" stroke-width="1.6"><rect x="6" y="2" width="28" height="42" rx="2"/><path d="M6 38h28M6 44v4h28M14 14h12M14 22h12"/><path d="M20 8c-2-2-5 1-2 3l2 2 2-2c3-2 0-5-2-3z"/></svg>
  <div><h4>3. Follow the story</h4><p>Walk between locations and solve clues.</p></div>
</div>
<div class="abs divider" style="top:2121px"></div>
<div class="abs step" style="top:2135px">
  <svg viewBox="0 0 42 50" fill="none" stroke="#1a7d8c" stroke-width="1.6"><path d="M10 4h22v12a11 11 0 0 1-22 0z"/><path d="M10 8H3c0 8 4 12 8 12M32 8h7c0 8-4 12-8 12M21 27v8M13 35h16v6H13zM9 47h24"/></svg>
  <div><h4>4. Have fun &amp; share</h4><p>Complete challenges and enjoy the experience.</p></div>
</div>

<div class="abs steps-photo-big" role="img" aria-label="Friends laughing together at a dinner table"></div>
<div class="abs steps-photo-small" role="img" aria-label="Group of young people reading a paper map outdoors"></div>
<div class="abs play">
  <svg width="14" height="16" viewBox="0 0 14 16"><path d="M2 1.5 12.5 8 2 14.5z" fill="#fff"/></svg>
</div>

<!-- Safe, social -->
<div class="abs safe-photo" role="img" aria-label="Smiling young woman holding a phone"></div>
<h2 class="abs heading safe-title">Safe, social,<br>and fun</h2>
<ul class="abs bullets">
  <li><span><svg width="7" height="7" viewBox="0 0 7 7"><path d="M1 3.5 3 5.5 6 1.5" stroke="#fff" stroke-width="1.3" fill="none"/></svg></span>Hundreds of groups already playing across multiple cities.</li>
  <li><span><svg width="7" height="7" viewBox="0 0 7 7"><path d="M1 3.5 3 5.5 6 1.5" stroke="#fff" stroke-width="1.3" fill="none"/></svg></span>Fully guided in-app instructions, no host required.</li>
  <li><span><svg width="7" height="7" viewBox="0 0 7 7"><path d="M1 3.5 3 5.5 6 1.5" stroke="#fff" stroke-width="1.3" fill="none"/></svg></span>Designed for friends, families, and teams of all sizes.</li>
</ul>

<!-- CTA -->
<div class="abs cta-outer"></div>
<div class="abs cta-inner" role="img" aria-label="Faint teal-tinted photo of friends outdoors"></div>
<h2 class="abs heading cta-title">Ready to play<br>in Bristol?</h2>
<div class="abs store store-light" style="left:608px;top:2762px;width:144px;height:43px"><i class="dot"></i><div><small>Get it on</small><b>App Shelf</b></div></div>
<div class="abs store store-light" style="left:763px;top:2762px;width:145px;height:43px;padding-left:40px"><div><small>Download on the</small><b>Play Hub</b></div></div>

<!-- Footer -->
<footer>
  <div class="abs foot-logo">vask</div>

  <div class="abs foot-col" style="left:419px;top:2976px">
    <h5>Company</h5>
    Home<br>How it Works<br>Features<br>Download<br>Locations
  </div>

  <div class="abs foot-col" style="left:574px;top:2976px">
    <h5>Contact us</h5>
    <div class="contact-item">
      <svg width="11" height="11" viewBox="0 0 11 11"><path d="M2 1h2l1 3-1.5 1a6 6 0 0 0 2.5 2.5L7 6l3 1v2a1 1 0 0 1-1 1A8 8 0 0 1 1 2a1 1 0 0 1 1-1z" fill="#2f9fb0"/></svg>
      <div><small>Phone*</small>+00 555 010 200</div>
    </div>
    <div class="contact-item" style="margin-top:12px">
      <svg width="11" height="11" viewBox="0 0 11 11"><rect x="0.5" y="2" width="10" height="7" fill="#2f9fb0"/><path d="M0.5 2 5.5 6l5-4" stroke="#30353b" fill="none"/></svg>
      <div><small>Email*</small>hello@vaskplay.test</div>
    </div>
    <div class="contact-item" style="margin-top:12px">
      <svg width="11" height="11" viewBox="0 0 11 11"><path d="M5.5 10S2 6.5 2 4a3.5 3.5 0 0 1 7 0c0 2.5-3.5 6-3.5 6z" fill="#2f9fb0"/><circle cx="5.5" cy="4" r="1.2" fill="#30353b"/></svg>
      <div><small>Location*</small>12 Harbour Lane, Suite<br>40, Portview 10234</div>
    </div>
  </div>

  <div class="abs foot-col" style="left:784px;top:2976px">
    <h5>Links</h5>
    Terms &amp; Condition<br>Privacy Policy<br>Disclaimer<br>Sitemap<br>Certification
  </div>

  <div class="abs foot-col" style="left:923px;top:2976px"><h5>Flow us</h5></div>
  <div class="abs social" style="left:924px"><span></span></div>
  <div class="abs social" style="left:973px"><span></span></div>
  <div class="abs social" style="left:1021px"><span></span></div>

  <div class="abs foot-line"></div>
  <p class="abs copyright">Copyright © 2026 Vask. All rights reserved</p>

  <div class="abs chat">
    <svg width="24" height="22" viewBox="0 0 24 22"><path d="M12 2C6.5 2 2 5.8 2 10.5c0 2.4 1.2 4.6 3.1 6.1L4 20l4.3-2c1.2.4 2.4.6 3.7.6 5.5 0 10-3.8 10-8.5S17.5 2 12 2z" fill="#fff"/><circle cx="8" cy="10.5" r="1.3" fill="#1a7d8c"/><circle cx="12" cy="10.5" r="1.3" fill="#1a7d8c"/><circle cx="16" cy="10.5" r="1.3" fill="#1a7d8c"/></svg>
  </div>
</footer>

</body>
</html>
```